Business Card: RW Office Partners - Your tidy answer finder

Business Name: RW Office Partners
Website: www.rwofficepartners.com.au
Email: marisol@rwofficepartners.com.au
Mobile: 61 487 902 346
Facebook: @rwofficepartners
Instrgram: @rwofficepartners

Brading Colours:
HEX
#986474
#ddccd3
#7a8498
#c9d8e4
#000000
#ffffff

Tag Line: Your organised problem solver

Link to DRAFT website:
https://helpdeskhub.sitebuilderx.com/rw-office-partners

About Page from the website:
My name is Marisol Bramwell, and I would love to assist you to become more productive in your day to day and achieve your business and personal goals.
My mission is to give you time, time to work on the important tasks of your business or to be able to spend more time with your family. I will take on the tasks you don’t have time for, don’t know well or simply don’t like to do.
I have an extensive background in Administration, Tender Coordination, Document Control, WHS and Quality Management working primarily in the Construction, Mining and Corporate World.
I am passionate about being organised, having order and making things in your life (and mine) easier! I love to watch something unfold and grow into something amazing! I am known for being the go-to problem solver, the organiser of all things, producing high standards of work even under pressure. I’m also a confident communicator, and I understand that you’re busy running your business.

Target Market(s)

Small to Medium Business who require assistance in their business by a virtual assistant.

Industry/Entity Type

Virtual Assistant

Contact Information for Business Card

Mobile: 61 487 902 346

Font styles to use
Sans Serif

Colors
ffffff

Requirements
Must have
• Branding Colours as outlined.
Contact Details as outlined.
Logo as provided.
Proper contact details - mobile, facebook, instragm, website.
Simple, Elegant, very clean looking.
Should not have
• Note cute with pictures.
Not too girly as still want to market to construction companies.

```html
<!DOCTYPE html>
<html lang="en">
<head>
<meta charset="utf-8">
<title>RW Office Partners – Business Card</title>
<link rel="stylesheet" href="https://fonts.googleapis.com/css2?family=Montserrat:wght@600;700&family=Open+Sans:wght@400;600&display=swap">
<style>
  :root {
    --mauve: #986474;
    --mauve-light: #ddccd3;
    --slate: #7a8498;
    --mist: #c9d8e4;
    --ink: #000000;
    --paper: #ffffff;
    --backdrop: #ecebed;
    --text-dark: #2b2b2f;
  }
  * { box-sizing: border-box; margin: 0; padding: 0; }
  html, body { width: 1200px; height: 892px; overflow: hidden; }
  body {
    background: var(--backdrop);
    display: flex;
    align-items: center;
    justify-content: center;
    gap: 40px;
    font-family: "Open Sans", Arial, sans-serif;
  }
  .card {
    position: relative;
    width: 540px;
    height: 330px;
    overflow: hidden;
    box-shadow: 0 6px 22px rgba(0,0,0,0.12);
  }

  /* Front */
  .card-front { background: var(--paper); }
  .accent-block {
    position: absolute; left: 0; top: 34px;
    width: 46px; height: 28px;
    background: var(--slate);
  }
  .holder-name {
    position: absolute; left: 64px; top: 34px;
    font-family: "Montserrat", Arial, sans-serif;
    font-weight: 700; font-size: 22px; letter-spacing: 0.5px;
    color: var(--mauve); text-transform: uppercase;
    line-height: 28px;
  }
  .accent-bar {
    position: absolute; left: 330px; right: 0; top: 52px;
    height: 28px; background: var(--slate);
  }
  .brand-lockup {
    position: absolute; left: 34px; top: 146px; width: 190px;
  }
  .brand-name {
    font-family: "Montserrat", Arial, sans-serif;
    font-weight: 700; font-size: 17px; line-height: 1.15;
    color: var(--mauve); text-transform: uppercase;
  }
  .brand-tagline {
    margin-top: 5px;
    font-size: 7.5px; letter-spacing: 2px;
    color: var(--slate); text-transform: uppercase;
  }
  .divider {
    position: absolute; left: 240px; top: 132px;
    width: 2px; height: 86px; background: var(--slate);
  }
  .contact-list {
    position: absolute; left: 258px; top: 140px;
    list-style: none;
  }
  .contact-list li {
    display: flex; align-items: center; gap: 10px;
    font-size: 13.5px; color: var(--text-dark);
    height: 25px;
  }
  .contact-list svg { width: 15px; height: 15px; flex: none; }
  .band {
    position: absolute; left: 0; right: 0;
    background: var(--mauve);
  }
  .band-upper { top: 232px; height: 22px; }
  .band-lower { top: 296px; height: 20px; }
  .social-row {
    position: absolute; left: 0; right: 0; top: 258px;
    height: 34px;
    display: flex; justify-content: center; gap: 70px; align-items: center;
  }
  .social-handle {
    display: flex; align-items: center; gap: 8px;
    font-size: 13.5px; color: var(--text-dark);
  }
  .social-dot {
    width: 14px; height: 14px; border-radius: 50%;
    background: var(--text-dark);
  }

  /* Back */
  .card-back {
    background: var(--mauve);
    display: flex; align-items: center; justify-content: center;
  }
  .frame {
    position: absolute; inset: 24px;
    border: 2px solid var(--mauve-light);
  }
  .back-lockup { text-align: center; color: var(--paper); }
  .back-name {
    font-family: "Montserrat", Arial, sans-serif;
    font-weight: 700; font-size: 38px; line-height: 1.1;
    text-transform: uppercase; letter-spacing: 1px;
  }
  .back-tagline {
    margin-top: 14px;
    font-size: 12px; letter-spacing: 4px;
    text-transform: uppercase;
  }
</style>
</head>
<body>

  <section class="card card-front" aria-label="Business card front">
    <div class="accent-block"></div>
    <h1 class="holder-name">Marisol Bramwell</h1>
    <div class="accent-bar"></div>

    <div class="brand-lockup">
      <p class="brand-name">RW Office<br>Partners</p>
      <p class="brand-tagline">Your tidy answer finder</p>
    </div>

    <div class="divider"></div>

    <ul class="contact-list">
      <li>
        <svg viewBox="0 0 16 16" aria-hidden="true" fill="none" stroke="#986474" stroke-width="1.4">
          <circle cx="8" cy="8" r="6.5"/><ellipse cx="8" cy="8" rx="2.8" ry="6.5"/><path d="M1.5 8h13M2.6 4.6h10.8M2.6 11.4h10.8"/>
        </svg>
        www.rwofficepartners.com.au
      </li>
      <li>
        <svg viewBox="0 0 16 16" aria-hidden="true">
          <rect x="1" y="3" width="14" height="10" fill="#986474"/><path d="M1 3l7 6 7-6" fill="none" stroke="#fff" stroke-width="1.2"/>
        </svg>
        marisol@rwofficepartners.com.au
      </li>
      <li>
        <svg viewBox="0 0 16 16" aria-hidden="true">
          <path d="M3.5 1.5l2.5 0 1 3.5-1.7 1.2a8 8 0 0 0 4.5 4.5L11 9l3.5 1v2.5c0 1-1 2-2 2C6.5 14.5 1.5 9.5 1.5 3.5c0-1 1-2 2-2z" fill="#986474"/>
        </svg>
        61 487 902 346
      </li>
    </ul>

    <div class="band band-upper"></div>
    <div class="social-row">
      <span class="social-handle"><span class="social-dot" aria-hidden="true"></span>@rwofficepartners</span>
      <span class="social-handle"><span class="social-dot" aria-hidden="true"></span>@rwofficepartners</span>
    </div>
    <div class="band band-lower"></div>
  </section>

  <section class="card card-back" aria-label="Business card back">
    <div class="frame"></div>
    <div class="back-lockup">
      <p class="back-name">RW Office<br>Partners</p>
      <p class="back-tagline">Your tidy answer finder</p>
    </div>
  </section>

</body>
</html>
```